Visitenkarte erstellen für Reiki Praxis

Visitenkarten für Reiki Praxis Doppelseitig

business cards reiki practice double-sided

The background can also be a different color

```html
<!DOCTYPE html>
<html lang="en">
<head>
<meta charset="utf-8">
<title>Lumen Balance – Business Cards</title>
<link rel="stylesheet" href="https://fonts.googleapis.com/css2?family=Montserrat:wght@600&family=Open+Sans:wght@400;600&display=swap">
<style>
  :root {
    --canvas-bg: #2a2a2a;
    --card-black: #1b1b1c;
    --pattern-dark: #232324;
    --pattern-light: #2c2b2d;
    --gold: #e2b22c;
    --gold-soft: #d8b36a;
    --rose: #c86fa0;
    --white: #f4f2f0;
    --divider: #6b4d5c;
  }
  * { box-sizing: border-box; margin: 0; padding: 0; }
  html, body { width: 1200px; height: 900px; overflow: hidden; }
  body {
    background: var(--canvas-bg);
    font-family: "Open Sans", Arial, sans-serif;
    display: flex;
    flex-direction: column;
    align-items: center;
    justify-content: center;
    gap: 36px;
  }
  .card {
    position: relative;
    width: 700px;
    height: 400px;
    border-radius: 14px;
    background: var(--card-black);
    overflow: hidden;
    box-shadow: 0 10px 30px rgba(0,0,0,.45);
  }
  /* back side */
  .card-back__pattern {
    position: absolute;
    inset: 0;
    background: radial-gradient(ellipse at 70% 30%, var(--pattern-light), var(--pattern-dark) 70%);
  }
  /* front side */
  .card-front { border-bottom: 8px solid var(--gold); }
  .brand {
    position: absolute;
    left: 0; right: 0; top: 78px;
    text-align: center;
  }
  .brand__name {
    display: inline-flex;
    align-items: center;
    gap: 12px;
    color: var(--white);
    font-size: 34px;
    font-weight: 400;
    letter-spacing: 1px;
    text-transform: uppercase;
  }
  .brand__dot {
    width: 14px; height: 14px;
    border-radius: 50%;
    background: var(--gold-soft);
  }
  .brand__owner {
    margin-top: 4px;
    color: var(--gold);
    font-size: 20px;
    letter-spacing: 8px;
    text-transform: uppercase;
  }
  .person {
    position: absolute;
    right: 380px; top: 228px;
    text-align: right;
  }
  .person__name {
    font-family: "Montserrat", Arial, sans-serif;
    font-weight: 600;
    font-size: 26px;
    color: var(--rose);
    letter-spacing: .5px;
    text-transform: uppercase;
  }
  .person__role { color: var(--white); font-size: 17px; }
  .divider {
    position: absolute;
    left: 342px; top: 214px;
    width: 1px; height: 82px;
    background: var(--divider);
  }
  .contacts {
    position: absolute;
    left: 364px; top: 212px;
    list-style: none;
    color: var(--white);
    font-size: 16px;
    line-height: 28px;
  }
  .contacts li { display: flex; align-items: center; gap: 8px; }
  .contacts svg { width: 14px; height: 14px; fill: var(--gold); flex: none; }
  .address {
    position: absolute;
    left: 0; right: 0; top: 330px;
    text-align: center;
    color: var(--white);
    font-size: 16px;
  }
</style>
</head>
<body>
  <section class="card card-back">
    <div class="card-back__pattern" role="img" aria-label="Repeating tone-on-tone lotus pattern covering the back of the card"></div>
  </section>

  <section class="card card-front">
    <div class="brand">
      <div class="brand__name"><span class="brand__dot"></span>Lumen Balance</div>
      <div class="brand__owner">Anna Verle</div>
    </div>

    <div class="person">
      <div class="person__name">Clara Weiss</div>
      <div class="person__role">Founder/CEO</div>
    </div>

    <div class="divider"></div>

    <ul class="contacts">
      <li>
        <svg viewBox="0 0 24 24" aria-hidden="true"><path d="M6.6 10.8a15.1 15.1 0 0 0 6.6 6.6l2.2-2.2a1 1 0 0 1 1-.25 11.4 11.4 0 0 0 3.6.57 1 1 0 0 1 1 1V20a1 1 0 0 1-1 1A17 17 0 0 1 3 4a1 1 0 0 1 1-1h3.5a1 1 0 0 1 1 1c0 1.25.2 2.45.57 3.57a1 1 0 0 1-.25 1z"/></svg>
        (555) 012 3480
      </li>
      <li>
        <svg viewBox="0 0 24 24" aria-hidden="true"><path d="M2 5h20v14H2z M4 7v.4l8 5 8-5V7l-8 5z" fill-rule="evenodd"/></svg>
        info@lumenbalance.com
      </li>
      <li>
        <svg viewBox="0 0 24 24" aria-hidden="true"><path d="M12 2a10 10 0 1 0 0 20 10 10 0 0 0 0-20zm0 2c.9 1.2 1.6 2.6 2 4h-4c.4-1.4 1.1-2.8 2-4zM4.3 14a8 8 0 0 1 0-4h3.4a16 16 0 0 0 0 4zm.9 2h3c.3 1.3.8 2.5 1.4 3.6A8 8 0 0 1 5.2 16zM8.2 8h-3a8 8 0 0 1 4.4-3.6C9 5.5 8.5 6.7 8.2 8zM12 20c-.9-1.2-1.6-2.6-2-4h4c-.4 1.4-1.1 2.8-2 4zm2.3-6H9.7a14 14 0 0 1 0-4h4.6a14 14 0 0 1 0 4zm.1 5.6c.6-1.1 1.1-2.3 1.4-3.6h3a8 8 0 0 1-4.4 3.6zm1.9-5.6a16 16 0 0 0 0-4h3.4a8 8 0 0 1 0 4z"/></svg>
        www.lumenbalance.com
      </li>
    </ul>

    <p class="address">2108 Linden Road Sample Town CD 51230</p>
  </section>
</body>
</html>
```